Copper Lantern Podcast Business Card Design

Needing a business card with the logo design provided for Copper Lantern Podcast. I am looking for a modern style that fits the current logo.

Info:
Name: Bao Khanh
Title: Creator/Host
Email: bao@copperlanternpod.com
Phone: (405) 637-2918
www.copperlanternpod.com
Twitter: @coplanternpod
Instagram: @copperlanternpodcast
Facebook: Copper Lantern Podcast

Industry/Entity Type

Business

Font styles to use
Sans Serif

Colors
000000
ffffff

Requirements
Must have
• modern, clean design
Nice to have
• social media contact info

```html
<!DOCTYPE html>
<html lang="en">
<head>
<meta charset="utf-8">
<title>Copper Lantern Podcast – Business Card</title>
<link rel="stylesheet" href="https://fonts.googleapis.com/css2?family=Open+Sans:wght@400;700&display=swap">
<style>
  :root {
    --backdrop: #8e8e8e;
    --card-dark: #1f1f1f;
    --card-light: #f2f2f4;
    --ink: #111111;
    --foil: #d4d4d4;
    --rule: #222222;
  }
  * { box-sizing: border-box; margin: 0; padding: 0; }
  html, body {
    width: 1200px; height: 781px; overflow: hidden;
    background: var(--backdrop);
    font-family: "Open Sans", Arial, sans-serif;
    color: var(--ink);
  }
  .canvas { position: relative; width: 1200px; height: 781px; }
  .card {
    position: absolute; left: 358px; width: 453px; height: 251px;
  }
  .card--front {
    top: 103px; background: var(--card-dark);
    display: flex; align-items: center; justify-content: center;
  }
  .front-name {
    color: var(--foil); font-weight: 700; font-size: 30px;
    letter-spacing: 0.5px; text-align: center; line-height: 1.1;
  }
  .card--back { top: 410px; background: var(--card-light); }
  .brand {
    position: absolute; left: 20px; top: 96px; width: 172px;
    text-align: center; font-weight: 700; font-size: 19px; line-height: 1.15;
    color: var(--ink);
  }
  .divider {
    position: absolute; left: 215px; top: 59px; width: 1.5px; height: 131px;
    background: var(--rule);
  }
  .contact { position: absolute; left: 239px; top: 58px; }
  .contact__name { font-weight: 700; font-size: 14.5px; line-height: 1.3; }
  .contact__title { font-size: 11px; margin-bottom: 9px; }
  .contact__list { list-style: none; font-size: 11px; line-height: 14.6px; }
  .contact__list + .contact__list { margin-top: 7px; }
  .contact__list li { display: flex; align-items: center; gap: 6px; }
  .icon { width: 9px; height: 9px; flex: none; }
  .icon--social { background: var(--ink); }
</style>
</head>
<body>
<div class="canvas">
  <section class="card card--front">
    <p class="front-name">Copper Lantern</p>
  </section>

  <section class="card card--back">
    <p class="brand">Copper Lantern Podcast</p>
    <div class="divider"></div>
    <div class="contact">
      <p class="contact__name">Bao Khanh</p>
      <p class="contact__title">Creator/Host</p>
      <ul class="contact__list">
        <li>
          <svg class="icon" viewBox="0 0 10 10"><path d="M2 1l2 2-1 1.2c.6 1.2 1.6 2.2 2.8 2.8L7 6l2 2-1.3 1.3C4.5 9 1 5.5.7 2.3z" fill="#111"/></svg>
          (405) 637-2918
        </li>
        <li>
          <svg class="icon" viewBox="0 0 10 10"><rect x="0.5" y="2" width="9" height="6.5" fill="none" stroke="#111" stroke-width="1.2"/><path d="M.5 2.3L5 5.6l4.5-3.3" fill="none" stroke="#111" stroke-width="1.2"/></svg>
          bao@copperlanternpod.com
        </li>
        <li>
          <svg class="icon" viewBox="0 0 10 10"><circle cx="5" cy="5" r="4.3" fill="none" stroke="#111" stroke-width="1"/><ellipse cx="5" cy="5" rx="1.8" ry="4.3" fill="none" stroke="#111" stroke-width="0.9"/><path d="M.7 5h8.6" stroke="#111" stroke-width="0.9"/></svg>
          www.copperlanternpod.com
        </li>
      </ul>
      <ul class="contact__list">
        <li><span class="icon icon--social"></span>@coplanternpod</li>
        <li><span class="icon icon--social"></span>@copperlanternpodcast</li>
        <li><span class="icon icon--social"></span>Copper Lantern Podcast</li>
      </ul>
    </div>
  </section>
</div>
</body>
</html>
```